Naturopath specialising in Children's Health

I have just started working in a new clinic where I will be predominantly treating children so I would like to rebrand with a business card that reflects this.

I would like a clever design which is subtly playful and will attract children and parents alike, while maintaining a professional look. It must also reflect that I utilize natural medicine - including herbal medicine and nutrition as part of my treatment. Employing the use of a plant or herb would be ideal. I had envisioned the image of a dandelion blowing in the wind (or being blown by a child) as a great combination of the playful yet natural medicine I am trying to ecompass in the card.

I would like to use yellow, orange, blue or green as the dominant colour for the card.

The front of the card should contain the logo and the words 'Maribel Stroud - Naturopath.'

The back of the card should contain the following details:
Maribel Stroud BHSc Nat, Dip RM
Naturopath, Herbalist, Nutritionist, Iridologist, Remedial Massage Therapist, Reiki Practitioner
0417 382 961
Thistle Kenwick - (02) 9463 1508
maribel.stroud@fernmail.example
HWPA 47183

```html
<!DOCTYPE html>
<html lang="en">
<head>
<meta charset="utf-8">
<title>Maribel Stroud – Naturopath Business Cards</title>
<link rel="stylesheet" href="https://fonts.googleapis.com/css2?family=Questrial&family=Open+Sans:wght@400;600&family=Lobster+Two:ital,wght@1,700&display=swap">
<style>
  :root {
    --bg: #f2f2f2;
    --card-white: #ffffff;
    --ink: #1e1e1e;
    --ink-soft: #4a4a4a;
    --green: #3f9a3a;
    --green-dark: #2a7030;
    --green-bright: #62b846;
    --white: #ffffff;
  }
  * { box-sizing: border-box; margin: 0; padding: 0; }
  html, body { width: 1200px; height: 1000px; overflow: hidden; }
  body {
    background: var(--bg);
    position: relative;
    font-family: "Open Sans", sans-serif;
    color: var(--ink);
  }

  /* Contact card (landscape, white) */
  .card-contact {
    position: absolute;
    left: 90px; top: 260px;
    width: 600px; height: 340px;
    background: var(--card-white);
    overflow: hidden;
  }
  .card-contact .holder-name {
    position: absolute; left: 38px; top: 30px;
    font-family: "Questrial", sans-serif;
    font-weight: 400;
    font-size: 38px; letter-spacing: 0.5px;
  }
  .card-contact .credentials {
    position: absolute; left: 48px; top: 80px;
    font-size: 16px; font-weight: 600; letter-spacing: 0.3px;
  }
  .card-contact .roles {
    position: absolute; left: 48px; top: 106px;
    width: 330px;
    font-size: 12px; line-height: 1.45;
    color: var(--ink-soft);
  }
  .brand-mark {
    position: absolute;
    display: flex; align-items: center; gap: 10px;
    font-family: "Questrial", sans-serif;
  }
  .card-contact .brand-mark {
    left: 48px; top: 220px;
    color: var(--green); font-size: 20px;
  }
  .brand-mark .dot {
    width: 26px; height: 26px; border-radius: 50%;
    background: currentColor; flex: none;
  }
  .contact-details {
    position: absolute; right: 34px; top: 160px;
    text-align: right; line-height: 1.5;
    font-size: 14.5px; letter-spacing: 0.2px;
  }
  .contact-details .mobile {
    font-size: 24px; letter-spacing: 1px; margin-bottom: 6px;
  }
  .card-contact .base-band {
    position: absolute; left: 0; right: 0; bottom: 0; height: 12px;
    background: linear-gradient(90deg, var(--green-dark), var(--green-bright));
  }

  /* Front card (portrait, green) */
  .card-front {
    position: absolute;
    left: 760px; top: 200px;
    width: 340px; height: 600px;
    background: linear-gradient(90deg, var(--green-dark), var(--green-bright));
    overflow: hidden;
    color: var(--white);
    text-align: center;
  }
  .card-front .holder-name {
    margin-top: 62px;
    font-family: "Questrial", sans-serif;
    font-size: 28px; letter-spacing: 0.5px;
  }
  .card-front .profession {
    font-family: "Lobster Two", cursive;
    font-style: italic; font-weight: 700;
    font-size: 44px; letter-spacing: 1px;
    margin-top: -4px;
  }
  .card-front .brand-mark {
    left: 0; right: 0; top: 290px;
    justify-content: center;
    color: var(--white); font-size: 24px;
  }
  .card-front .light-stripe {
    position: absolute; left: 0; right: 0; bottom: 56px; height: 16px;
    background: var(--white);
  }
</style>
</head>
<body>

  <section class="card-contact" aria-label="Business card, contact side">
    <h1 class="holder-name">Maribel Stroud</h1>
    <p class="credentials">BHSc Nat, Dip RM</p>
    <p class="roles">Naturopath, Herbalist, Nutritionist, Iridologist, Remedial Massage Therapist, Reiki Practitioner</p>
    <div class="brand-mark"><span class="dot"></span><span>Maribel Stroud</span></div>
    <div class="contact-details">
      <p class="mobile">0417 382 961</p>
      <p>Thistle Kenwick - (02) 9463 1508</p>
      <p>maribel.stroud@fernmail.example</p>
      <p>HWPA 47183</p>
    </div>
    <div class="base-band"></div>
  </section>

  <section class="card-front" aria-label="Business card, front side">
    <p class="holder-name">Maribel Stroud</p>
    <p class="profession">Naturopath</p>
    <div class="brand-mark"><span class="dot"></span><span>Maribel Stroud</span></div>
    <div class="light-stripe"></div>
  </section>

</body>
</html>
```